3 out of 100 people will get deadly skin cancer - we need a great illustration that shows this!

We put together a prototype image that communicates lifetime skin cancer risk. (see attached). We are looking for illustrators who can take make a new/better/cooler graphic that communicates this idea. It could be as simple as a superior illustration of the graphic we have or illustrators can propose a completely different idea.What should the illustration communicate?U.S. adults have a lifetime risk of developing skin cancer of 1 in 5. But we don't want to show 1 in 5; we want to show that number in a larger group. For example, in the attached illustration we show 20 in 100 people get skin cancer (i.e., 100 beach towels/umbrellas and 20 of them are red). Research has shown that people are more likely to accurately understand numbers like this when you convey them for larger groups (i.e., 20 out of 100 rather than 1 out of 5). U.S. adults also have a lifetime risk of 2.3% of developing the deadliest form of skin cancer (melanoma). In other words, approximately 3 in 100 people will develop melanoma in their lifetime. Ideally, a single image will convey both lifetime skin cancer risk (20 in 100) and melanoma risk (3 in 100). We will award a top three as follows: 1st place = $300, 2nd place = $250, third place = $200. We will also buy any design beyond 3rd place that we like for $100. For example, we purchased 24 designs in our last contest on Artmarketly.This research is supported by funding from the Corvane Institute of Science.

Target Market(s)

The U.S. public; individuals at high risk of developing skin cancer

Industry/Entity Type

Medicine

Colors

Designer to choose colors to be used in the design.

Requirements
Must have
• an original illustration that conveys both lifetime risk of developing skin cancer (20 in 100) and melanoma (3 in 100).
Nice to have
• It can be beach towels and umbrellas, just like our prototype, or the designers can pitch an original idea. Imagery can be realistic or cartoonish (or something in between). It should be illustrations, though. Not edited photos. The image should be in color (no black and white illustrations).
Should not have
• Photos. Clip art. Free vector images.
• We are looking for original illustrations created by the designer.

```html
<!DOCTYPE html>
<html lang="en">
<head>
<meta charset="utf-8">
<title>Skin Cancer – Lifetime Risk</title>
<link href="https://fonts.googleapis.com/css2?family=Rubik:wght@400;900&display=swap" rel="stylesheet">
<style>
  :root {
    --background: #e6cd9c;
    --title-pink: #f2558a;
    --towel-border: #62cdb9;
    --towel-cloth: #ede6d8;
    --figure-teal: #5cc4b6;
    --risk-red: #e8204f;
    --melanoma-dark: #3a2320;
    --card: #f7f5f0;
    --legend-text: #6f6f6f;
  }
  * { box-sizing: border-box; margin: 0; padding: 0; }
  html, body {
    width: 1200px;
    height: 2557px;
    overflow: hidden;
  }
  body {
    position: relative;
    background: var(--background);
    font-family: "Rubik", Arial, sans-serif;
  }
  .title {
    position: absolute;
    left: 74px;
    top: 62px;
    font-size: 162px;
    font-weight: 900;
    letter-spacing: -3px;
    line-height: 1;
    color: var(--title-pink);
    white-space: nowrap;
  }
  .legend-card {
    position: absolute;
    left: 912px;
    top: 244px;
    width: 260px;
    height: 240px;
    background: var(--card);
    padding: 22px 24px;
    display: flex;
    flex-direction: column;
    justify-content: space-between;
  }
  .legend-row {
    display: flex;
    align-items: center;
    gap: 16px;
    font-size: 15px;
  }
  .legend-icon { width: 24px; height: 56px; flex: none; }
  .no-cancer { color: var(--figure-teal); }
  .skin-cancer { color: var(--risk-red); }
  .melanoma { color: var(--melanoma-dark); }
  .legend-icon.no-cancer { fill: var(--figure-teal); }
  .legend-icon.skin-cancer { fill: var(--risk-red); }
  .legend-icon.melanoma { fill: var(--melanoma-dark); }
  .towel {
    position: absolute;
    left: 247px;
    top: 532px;
    width: 703px;
    height: 1040px;
    background: var(--towel-cloth);
    border: 14px solid var(--towel-border);
  }
  .risk-grid {
    position: absolute;
    left: 0;
    top: 0;
    width: 675px;
    height: 1012px;
  }
  .fig-none { fill: var(--figure-teal); }
  .fig-skin { fill: var(--risk-red); }
  .fig-mel { fill: var(--melanoma-dark); }
</style>
</head>
<body>
  <svg width="0" height="0" style="position:absolute" aria-hidden="true">
    <defs>
      <symbol id="person" viewBox="0 0 30 77">
        <circle cx="15" cy="7" r="7"/>
        <rect x="5" y="16" width="20" height="28" rx="3"/>
        <rect x="0" y="17" width="4" height="24" rx="2"/>
        <rect x="26" y="17" width="4" height="24" rx="2"/>
        <rect x="6" y="44" width="8" height="33" rx="2"/>
        <rect x="16" y="44" width="8" height="33" rx="2"/>
      </symbol>
    </defs>
  </svg>

  <h1 class="title">Skin Cancer</h1>

  <aside class="legend-card">
    <div class="legend-row"><svg class="legend-icon no-cancer" viewBox="0 0 30 77"><use href="#person"/></svg><span class="no-cancer">= no cancer</span></div>
    <div class="legend-row"><svg class="legend-icon skin-cancer" viewBox="0 0 30 77"><use href="#person"/></svg><span class="skin-cancer">= skin cancer</span></div>
    <div class="legend-row"><svg class="legend-icon melanoma" viewBox="0 0 30 77"><use href="#person"/></svg><span class="melanoma">= melanoma</span></div>
  </aside>

  <section class="towel">
    <svg class="risk-grid" viewBox="0 0 675 1012" role="img" aria-label="100 people: 80 with no cancer, 17 with skin cancer and 3 with melanoma">
      <g class="row" transform="translate(0,47)">
        <use href="#person" class="fig-skin" x="128" width="30" height="77"/>
        <use href="#person" class="fig-none" x="171" width="30" height="77"/>
        <use href="#person" class="fig-none" x="214" width="30" height="77"/>
        <use href="#person" class="fig-none" x="257" width="30" height="77"/>
        <use href="#person" class="fig-none" x="300" width="30" height="77"/>
        <use href="#person" class="fig-none" x="343" width="30" height="77"/>
        <use href="#person" class="fig-none" x="386" width="30" height="77"/>
        <use href="#person" class="fig-none" x="429" width="30" height="77"/>
        <use href="#person" class="fig-none" x="472" width="30" height="77"/>
        <use href="#person" class="fig-none" x="515" width="30" height="77"/>
      </g>
      <g class="row" transform="translate(0,133)">
        <use href="#person" class="fig-skin" x="128" width="30" height="77"/>
        <use href="#person" class="fig-none" x="171" width="30" height="77"/>
        <use href="#person" class="fig-none" x="214" width="30" height="77"/>
        <use href="#person" class="fig-none" x="257" width="30" height="77"/>
        <use href="#person" class="fig-none" x="300" width="30" height="77"/>
        <use href="#person" class="fig-none" x="343" width="30" height="77"/>
        <use href="#person" class="fig-skin" x="386" width="30" height="77"/>
        <use href="#person" class="fig-none" x="429" width="30" height="77"/>
        <use href="#person" class="fig-none" x="472" width="30" height="77"/>
        <use href="#person" class="fig-none" x="515" width="30" height="77"/>
      </g>
      <g class="row" transform="translate(0,219)">
        <use href="#person" class="fig-none" x="128" width="30" height="77"/>
        <use href="#person" class="fig-none" x="171" width="30" height="77"/>
        <use href="#person" class="fig-none" x="214" width="30" height="77"/>
        <use href="#person" class="fig-skin" x="257" width="30" height="77"/>
        <use href="#person" class="fig-none" x="300" width="30" height="77"/>
        <use href="#person" class="fig-none" x="343" width="30" height="77"/>
        <use href="#person" class="fig-mel" x="386" width="30" height="77"/>
        <use href="#person" class="fig-none" x="429" width="30" height="77"/>
        <use href="#person" class="fig-none" x="472" width="30" height="77"/>
        <use href="#person" class="fig-none" x="515" width="30" height="77"/>
      </g>
      <g class="row" transform="translate(0,305)">
        <use href="#person" class="fig-none" x="128" width="30" height="77"/>
        <use href="#person" class="fig-skin" x="171" width="30" height="77"/>
        <use href="#person" class="fig-none" x="214" width="30" height="77"/>
        <use href="#person" class="fig-none" x="257" width="30" height="77"/>
        <use href="#person" class="fig-none" x="300" width="30" height="77"/>
        <use href="#person" class="fig-skin" x="343" width="30" height="77"/>
        <use href="#person" class="fig-none" x="386" width="30" height="77"/>
        <use href="#person" class="fig-none" x="429" width="30" height="77"/>
        <use href="#person" class="fig-skin" x="472" width="30" height="77"/>
        <use href="#person" class="fig-none" x="515" width="30" height="77"/>
      </g>
      <g class="row" transform="translate(0,396)">
        <use href="#person" class="fig-none" x="128" width="30" height="77"/>
        <use href="#person" class="fig-skin" x="171" width="30" height="77"/>
        <use href="#person" class="fig-none" x="214" width="30" height="77"/>
        <use href="#person" class="fig-none" x="257" width="30" height="77"/>
        <use href="#person" class="fig-skin" x="300" width="30" height="77"/>
        <use href="#person" class="fig-none" x="343" width="30" height="77"/>
        <use href="#person" class="fig-none" x="386" width="30" height="77"/>
        <use href="#person" class="fig-none" x="429" width="30" height="77"/>
        <use href="#person" class="fig-none" x="472" width="30" height="77"/>
        <use href="#person" class="fig-none" x="515" width="30" height="77"/>
      </g>
      <g class="row" transform="translate(0,488)">
        <use href="#person" class="fig-none" x="128" width="30" height="77"/>
        <use href="#person" class="fig-skin" x="171" width="30" height="77"/>
        <use href="#person" class="fig-mel" x="214" width="30" height="77"/>
        <use href="#person" class="fig-none" x="257" width="30" height="77"/>
        <use href="#person" class="fig-none" x="300" width="30" height="77"/>
        <use href="#person" class="fig-none" x="343" width="30" height="77"/>
        <use href="#person" class="fig-none" x="386" width="30" height="77"/>
        <use href="#person" class="fig-none" x="429" width="30" height="77"/>
        <use href="#person" class="fig-none" x="472" width="30" height="77"/>
        <use href="#person" class="fig-none" x="515" width="30" height="77"/>
      </g>
      <g class="row" transform="translate(0,579)">
        <use href="#person" class="fig-none" x="128" width="30" height="77"/>
        <use href="#person" class="fig-none" x="171" width="30" height="77"/>
        <use href="#person" class="fig-none" x="214" width="30" height="77"/>
        <use href="#person" class="fig-none" x="257" width="30" height="77"/>
        <use href="#person" class="fig-skin" x="300" width="30" height="77"/>
        <use href="#person" class="fig-none" x="343" width="30" height="77"/>
        <use href="#person" class="fig-none" x="386" width="30" height="77"/>
        <use href="#person" class="fig-none" x="429" width="30" height="77"/>
        <use href="#person" class="fig-skin" x="472" width="30" height="77"/>
        <use href="#person" class="fig-none" x="515" width="30" height="77"/>
      </g>
      <g class="row" transform="translate(0,673)">
        <use href="#person" class="fig-none" x="128" width="30" height="77"/>
        <use href="#person" class="fig-none" x="171" width="30" height="77"/>
        <use href="#person" class="fig-none" x="214" width="30" height="77"/>
        <use href="#person" class="fig-none" x="257" width="30" height="77"/>
        <use href="#person" class="fig-skin" x="300" width="30" height="77"/>
        <use href="#person" class="fig-none" x="343" width="30" height="77"/>
        <use href="#person" class="fig-skin" x="386" width="30" height="77"/>
        <use href="#person" class="fig-none" x="429" width="30" height="77"/>
        <use href="#person" class="fig-none" x="472" width="30" height="77"/>
        <use href="#person" class="fig-none" x="515" width="30" height="77"/>
      </g>
      <g class="row" transform="translate(0,767)">
        <use href="#person" class="fig-none" x="128" width="30" height="77"/>
        <use href="#person" class="fig-none" x="171" width="30" height="77"/>
        <use href="#person" class="fig-none" x="214" width="30" height="77"/>
        <use href="#person" class="fig-none" x="257" width="30" height="77"/>
        <use href="#person" class="fig-mel" x="300" width="30" height="77"/>
        <use href="#person" class="fig-none" x="343" width="30" height="77"/>
        <use href="#person" class="fig-skin" x="386" width="30" height="77"/>
        <use href="#person" class="fig-none" x="429" width="30" height="77"/>
        <use href="#person" class="fig-none" x="472" width="30" height="77"/>
        <use href="#person" class="fig-none" x="515" width="30" height="77"/>
      </g>
      <g class="row" transform="translate(0,876)">
        <use href="#person" class="fig-skin" x="128" width="30" height="77"/>
        <use href="#person" class="fig-none" x="171" width="30" height="77"/>
        <use href="#person" class="fig-none" x="214" width="30" height="77"/>
        <use href="#person" class="fig-none" x="257" width="30" height="77"/>
        <use href="#person" class="fig-none" x="300" width="30" height="77"/>
        <use href="#person" class="fig-none" x="343" width="30" height="77"/>
        <use href="#person" class="fig-skin" x="386" width="30" height="77"/>
        <use href="#person" class="fig-none" x="429" width="30" height="77"/>
        <use href="#person" class="fig-none" x="472" width="30" height="77"/>
        <use href="#person" class="fig-none" x="515" width="30" height="77"/>
      </g>
    </svg>
  </section>
</body>
</html>
```